Political Candidate Newspaper Advertisement

I would like a newspaper ad for my campaign for election to City Council. The banner ad is 10 cm high x 26.2 cm wide. The banner will contain a photo and the following text (or words to similar effect):
VOTE
DENNIS HALE
COMO BEACH
For a
SAFE
CARING
CONNECTED
COMMUNITY
Lifetime commitment to local clubs, charities and international aid
Local business owner
Founder of Open-Gate Week
Councillor, Mediator, B.Sc., MBA
The Councillor you know and can call for help
Respects our heritage and our future
Listens to the wisdom and needs of older residents
Promotes more young people
Protects our South Perth environment
Authorised by Dennis Hale 5/348 Kelby Rd, Como. 9317 2864
I use MS Publisher and PhotoShop so I'd like the product to be in a form I can use. After ther banner ad is done, and if it is good, I wish to pay the designer to use the same theme to produce another newspaper ad, a brochure and a poster.
My simple version is attached. A photo is also attached.
I'm hoping you do better.
18-80 years old
Business
- simple fonts
- A TICK somewhere around the word Vote would be good.
Mention of www.fairlandward.notepage.net if possible, perhaps at the bottom of the page, along with the Authorised by ... text.

```html
<!DOCTYPE html>
<html lang="en">
<head>
<meta charset="utf-8">
<title>Vote Dennis Hale – Como Beach</title>
<link href="https://fonts.googleapis.com/css2?family=Archivo+Black&family=Oswald:wght@600&family=Barlow+Semi+Condensed:ital,wght@0,600;0,700;1,500&display=swap" rel="stylesheet">
<style>
  :root {
    --paper: #ffffff;
    --frame-green: #2fe02f;
    --field-blue: #0a2fc4;
    --campaign-red: #e00a0a;
    --tick-green: #22c41a;
    --text-white: #ffffff;
    --authorise-yellow: #f2e21a;
  }
  html, body {
    margin: 0;
    width: 1200px;
    height: 601px;
    overflow: hidden;
    background: var(--paper);
  }
  .canvas { position: relative; width: 1200px; height: 601px; }
  .banner {
    position: absolute;
    left: 76px; top: 98px;
    width: 1030px; height: 393px;
    box-sizing: border-box;
    border: 5px solid var(--frame-green);
    background: var(--field-blue);
    overflow: hidden;
  }
  .banner-art { position: absolute; left: 0; top: 0; }
  .slogan {
    position: absolute;
    right: 560px; top: 78px;
    margin: 0;
    text-align: right;
    color: var(--text-white);
    font-family: "Barlow Semi Condensed", sans-serif;
    font-weight: 700;
    text-shadow: 2px 2px 2px rgba(0,0,0,.45);
    line-height: 47px;
  }
  .slogan .lead { font-size: 28px; font-weight: 600; line-height: 36px; display: block; }
  .slogan .word { font-size: 35px; display: block; letter-spacing: 1px; }
  .credentials {
    position: absolute;
    left: 531px; top: 22px;
    margin: 0; padding: 0;
    list-style: none;
    color: var(--text-white);
    font-family: "Barlow Semi Condensed", sans-serif;
    font-weight: 700;
    font-size: 15px;
    line-height: 16px;
  }
  .credentials li {
    position: relative;
    padding-left: 33px;
    margin-bottom: 14px;
    width: 300px;
  }
  .credentials li::before {
    content: "";
    position: absolute; left: 0; top: -4px;
    width: 24px; height: 24px;
    border-radius: 50%;
    background: var(--text-white);
    box-shadow: 1px 1px 2px rgba(0,0,0,.5);
  }
  .credentials .tick-mark {
    position: absolute; left: 2px; top: -8px;
    width: 24px; height: 26px;
  }
  .credentials small { font-size: 12px; }
  .authorisation {
    position: absolute;
    right: 20px; bottom: 12px;
    margin: 0;
    color: var(--authorise-yellow);
    font-family: "Barlow Semi Condensed", sans-serif;
    font-style: italic;
    font-weight: 500;
    font-size: 11px;
  }
</style>
</head>
<body>
<div class="canvas">
  <section class="banner">
    <svg class="banner-art" width="1020" height="383" viewBox="0 0 1020 383">
      <defs>
        <filter id="drop" x="-20%" y="-20%" width="140%" height="140%">
          <feDropShadow dx="4" dy="5" stdDeviation="4" flood-color="#000" flood-opacity=".45"/>
        </filter>
        <linearGradient id="portrait-tone" x1="0" y1="0" x2="0" y2="1">
          <stop offset="0" stop-color="#2fe02f"/>
          <stop offset=".55" stop-color="#f4f6f2"/>
          <stop offset="1" stop-color="#d8c7bd"/>
        </linearGradient>
        <linearGradient id="ellipse-tone" x1="0" y1="0" x2="0" y2="1">
          <stop offset="0" stop-color="#ffffff"/>
          <stop offset="1" stop-color="#e4e4e4"/>
        </linearGradient>
      </defs>
      <!-- red top sweep -->
      <path d="M0,0 H405 Q360,110 235,150 Q120,185 0,190 Z" fill="var(--campaign-red)" filter="url(#drop)"/>
      <!-- large slogan disc -->
      <circle cx="327" cy="190" r="170" fill="var(--campaign-red)" filter="url(#drop)"/>
      <!-- suburb disc -->
      <circle cx="125" cy="262" r="68" fill="var(--campaign-red)" stroke="#ffffff" stroke-width="1" filter="url(#drop)"/>
      <text x="125" y="253" text-anchor="middle" font-family="Barlow Semi Condensed, sans-serif" font-weight="700" font-size="29" fill="#fff" style="text-shadow:2px 2px 2px rgba(0,0,0,.4)">COMO</text>
      <text x="125" y="285" text-anchor="middle" font-family="Barlow Semi Condensed, sans-serif" font-weight="700" font-size="29" fill="#fff">BEACH</text>
      <!-- name ellipse -->
      <ellipse cx="175" cy="142" rx="165" ry="72" fill="url(#ellipse-tone)" filter="url(#drop)"/>
      <text x="175" y="168" text-anchor="middle" font-family="Oswald, sans-serif" font-weight="600" font-size="62" fill="var(--campaign-red)" stroke="#7a0000" stroke-width="1.2" textLength="290" lengthAdjust="spacingAndGlyphs">Dennis Hale</text>
      <!-- VOTE -->
      <text x="25" y="60" font-family="Archivo Black, sans-serif" font-size="48" fill="#fff" stroke="#888" stroke-width="1" letter-spacing="2" filter="url(#drop)">VOTE</text>
      <!-- large tick -->
      <path d="M242,68 L256,56 L278,86 Q300,40 333,17 L340,25 Q304,60 281,110 Z" fill="var(--tick-green)" stroke="#0c7a0c" stroke-width="1.5" filter="url(#drop)"/>
      <!-- portrait area -->
      <circle cx="905" cy="165" r="122" fill="url(#portrait-tone)" role="img" aria-label="Portrait photo of candidate Dennis Hale in suit and tie"/>
    </svg>

    <p class="slogan">
      <span class="lead">For a</span>
      <span class="word">SAFE</span>
      <span class="word">CARING</span>
      <span class="word">CONNECTED</span>
      <span class="word">COMMUNITY</span>
    </p>

    <ul class="credentials">
      <li><svg class="tick-mark" viewBox="0 0 24 26"><path d="M3,13 L7,10 L11,16 Q15,6 22,1 L24,3 Q17,11 12,23 Z" fill="var(--tick-green)"/></svg>Lifetime commitment to local clubs, charities and international aid</li>
      <li><svg class="tick-mark" viewBox="0 0 24 26"><path d="M3,13 L7,10 L11,16 Q15,6 22,1 L24,3 Q17,11 12,23 Z" fill="var(--tick-green)"/></svg>Local business owner</li>
      <li><svg class="tick-mark" viewBox="0 0 24 26"><path d="M3,13 L7,10 L11,16 Q15,6 22,1 L24,3 Q17,11 12,23 Z" fill="var(--tick-green)"/></svg>Founder of Open-Gate Week</li>
      <li><svg class="tick-mark" viewBox="0 0 24 26"><path d="M3,13 L7,10 L11,16 Q15,6 22,1 L24,3 Q17,11 12,23 Z" fill="var(--tick-green)"/></svg>Councillor, Mediator, <small>B.Sc., MBA</small></li>
      <li><svg class="tick-mark" viewBox="0 0 24 26"><path d="M3,13 L7,10 L11,16 Q15,6 22,1 L24,3 Q17,11 12,23 Z" fill="var(--tick-green)"/></svg>The Councillor you know and<br>can call for help</li>
      <li><svg class="tick-mark" viewBox="0 0 24 26"><path d="M3,13 L7,10 L11,16 Q15,6 22,1 L24,3 Q17,11 12,23 Z" fill="var(--tick-green)"/></svg>Respects our heritage and<br>our future</li>
      <li><svg class="tick-mark" viewBox="0 0 24 26"><path d="M3,13 L7,10 L11,16 Q15,6 22,1 L24,3 Q17,11 12,23 Z" fill="var(--tick-green)"/></svg>Listens to the wisdom and needs<br>of older residents</li>
      <li><svg class="tick-mark" viewBox="0 0 24 26"><path d="M3,13 L7,10 L11,16 Q15,6 22,1 L24,3 Q17,11 12,23 Z" fill="var(--tick-green)"/></svg>Promotes more young people</li>
      <li><svg class="tick-mark" viewBox="0 0 24 26"><path d="M3,13 L7,10 L11,16 Q15,6 22,1 L24,3 Q17,11 12,23 Z" fill="var(--tick-green)"/></svg>Protects our South Perth environment</li>
    </ul>

    <p class="authorisation">Authorised by Dennis Hale 5/348 Kelby Rd, Como. 9317 2864</p>
  </section>
</div>
</body>
</html>
```